BW Business Card

Used Car Sales
We are trying to recreate the image of our license plate on business cards,
it is a red background with a white oval that is open on the ends
I attempted to upload the image but it was a dismal failure when the products arrived
the lettering was too small and the edges were white
I think maybe the red needs some texture in it, still red but something that doesn't look so flat
and maybe a beveled edge around the white (not sure)

Target Market(s)

Adults 25-65 that drive

Industry/Entity Type

Business

Contact Information for Business Card

Darlene Whitcombe, Sales Manager, BRIGHTWAY AUTO MART, INC., 462 Fernhill Road, Pulaski, TN 38591,
931 587-2064 (office), 931 587-6259 (fax) - We Finance everyone with approved credit
BrightwayAutoMart.Com

On Back: Financing Available - We Finance everyone with approved credit
Easy Payments: Monthly, Semi-Monthly or Weekly
Ask about our Layaway plan
Open Mon-Sat
8:30 AM - 5 PM

Requirements
Must have
• We want to match the license plate (minus holes for screws)

```html
<!DOCTYPE html>
<html lang="en">
<head>
<meta charset="utf-8">
<title>Brightway Auto Mart – Business Card</title>
<link href="https://fonts.googleapis.com/css2?family=Arimo:wght@400;700&display=swap" rel="stylesheet">
<style>
  :root {
    --page: #e9e7e4;
    --blue-light: #93a9d2;
    --blue-dark: #7089bd;
    --red: #e8333a;
    --red-deep: #d81f26;
    --band: #3b3b3d;
    --white: #ffffff;
    --ink: #2a2a2a;
  }
  * { box-sizing: border-box; margin: 0; padding: 0; }
  html, body { width: 1200px; height: 914px; overflow: hidden; }
  body {
    background: var(--page);
    font-family: "Arimo", Arial, sans-serif;
    position: relative;
  }
  .card {
    position: absolute;
    left: 260px;
    width: 680px;
    height: 389px;
    overflow: hidden;
    box-shadow: 0 6px 18px rgba(0,0,0,.18);
  }
  .card-back { top: 48px; background: var(--white); }
  .card-front {
    top: 477px;
    background: radial-gradient(ellipse at 45% 40%, var(--blue-light), var(--blue-dark) 85%);
    color: var(--white);
  }
  .card-shapes { position: absolute; inset: 0; width: 100%; height: 100%; }

  /* back */
  .back-copy {
    position: absolute;
    inset: 0;
    display: flex;
    flex-direction: column;
    align-items: center;
    justify-content: center;
    text-align: center;
    color: var(--ink);
    font-size: 19px;
    line-height: 1.3;
  }
  .back-copy .gap { height: 24px; }
  .back-copy .open { font-size: 24px; margin-top: 8px; }

  /* front */
  .brand-name {
    position: absolute;
    left: 40px;
    top: 120px;
    width: 250px;
    font-size: 27px;
    font-weight: 700;
    letter-spacing: 1px;
    line-height: 1.15;
    color: var(--white);
  }
  .divider {
    position: absolute;
    left: 312px;
    top: 60px;
    width: 1px;
    height: 240px;
    background: rgba(255,255,255,.75);
  }
  .person { position: absolute; left: 345px; top: 95px; }
  .person-name { font-size: 25px; font-weight: 400; letter-spacing: 1px; text-transform: uppercase; }
  .person-title { font-size: 17px; margin-top: 2px; opacity: .92; }
  .contact-list { list-style: none; position: absolute; left: 345px; top: 195px; font-size: 18px; line-height: 1.45; }
  .contact-list li { display: flex; align-items: center; gap: 8px; }
  .contact-list svg { width: 17px; height: 17px; flex: none; }
  .tagline-band {
    position: absolute;
    left: 0; bottom: 0;
    width: 100%; height: 62px;
    background: var(--band);
    display: flex;
    align-items: center;
    padding-left: 30px;
    font-size: 20px;
    letter-spacing: .3px;
  }
</style>
</head>
<body>

<section class="card card-back" aria-label="Card back">
  <svg class="card-shapes" viewBox="0 0 680 389" preserveAspectRatio="none" aria-hidden="true">
    <path d="M0 0 L0 62 Q110 22 250 0 Z" fill="var(--red)"/>
    <path d="M680 318 Q560 350 390 389 L680 389 Z" fill="var(--red-deep)"/>
  </svg>
  <div class="back-copy">
    <p>Financing Available</p>
    <p>We Finance everyone with approved credit</p>
    <p>Easy Payments: Monthly, Semi-Monthly or Weekly</p>
    <div class="gap"></div>
    <p>Ask about our Layaway plan</p>
    <div class="gap"></div>
    <p class="open">Open</p>
    <p>Mon-Sat 8:30 AM - 5 PM</p>
  </div>
</section>

<section class="card card-front" aria-label="Card front">
  <svg class="card-shapes" viewBox="0 0 680 389" preserveAspectRatio="none" aria-hidden="true">
    <path d="M470 0 Q625 60 680 235 L680 0 Z" fill="var(--red)"/>
    <path d="M0 205 Q45 285 115 327 L0 327 Z" fill="var(--red)"/>
  </svg>

  <p class="brand-name">BRIGHTWAY<br>AUTO MART</p>
  <div class="divider"></div>

  <div class="person">
    <p class="person-name">Darlene Whitcombe</p>
    <p class="person-title">Sales Manager</p>
  </div>

  <ul class="contact-list">
    <li>
      <svg viewBox="0 0 20 20" aria-hidden="true"><rect width="20" height="20" rx="2" fill="#fff"/><path d="M5 6c0-1 1-2 2-2h6c1 0 2 1 2 2v1h-3V6H8v1H5z M6 9h8l1 6H5z" fill="var(--blue-dark)"/></svg>
      931 587-2064
    </li>
    <li>
      <svg viewBox="0 0 20 20" aria-hidden="true"><rect width="20" height="20" rx="2" fill="#fff"/><path d="M6 4h8v4H6z M4 9h12v6h-2v-3H6v3H4z M7 13h6v3H7z" fill="var(--blue-dark)"/></svg>
      931 587-6259
    </li>
    <li>
      <svg viewBox="0 0 20 20" aria-hidden="true"><rect width="20" height="20" rx="2" fill="#fff"/><path d="M10 3a5 5 0 0 1 5 5c0 4-5 9-5 9s-5-5-5-9a5 5 0 0 1 5-5z" fill="var(--blue-dark)"/><circle cx="10" cy="8" r="2" fill="#fff"/></svg>
      462 Fernhill Road, Pulaski, TN 38591
    </li>
  </ul>

  <div class="tagline-band">We Finance everyone with approved credit&nbsp;&nbsp;BrightwayAutoMart.Com</div>
</section>

</body>
</html>
```